Mobile Charts

Context:
I have built a mobile app using flex that shows charts based on some selections. It has 2 screens (Attached), the slash screen and the graphs screen. I also attached the photoshop file for the splash screen. The company name is "Plorvex", the product name is "Amber Kite"

I need to take the design to the next level as far as professionalism. The look should match some top analytics companies products. It should exude precision and professionalism.

Most rework will be done with the splash screen (photo shop attached). The splash screen is a 840 by 690) png that contains the instruction text as well as the Product logo and company logo.

Specific deliverables in order (feel free to do only the top 3, bonus points for the others):
1. Product Icon for "Amber Kite". The current icon being used is just a place holder (on the splash screen). We need something simple that will work in both the splash screen and to launch the application.
It should be this image: http://www.grivolart.example/file/red-sphere.jpg
with a white "AK" inside of it.

2. Company Logo for Plorvex. The current font being used works ok, but maybe something with more flare. Whatever you come up with should be in the splash screen.

3. Better placement / font selection / font size for the instructions. Maybe a box around each instruction as well. Feel free to kill the carrots/arrows.

4. Font selection: Which font family/ size/ color would you recommend for each text outside of the splash screen.

5. Button shape/color changes: Whats a better look for the list buttons or back button. If you make a change here I need pngs for the up and selected state.

Target Market(s)

executives at companies that develop games or freemium apps

Industry/Entity Type

Shop

Font styles to use
Sans Serif

Colors
ec2027
ffffff

Requirements
Must have
• Must look clean / professional. Product logo, company logo, new splash page.
Nice to have
• font selections

```html
<!DOCTYPE html>
<html lang="en">
<head>
<meta charset="utf-8">
<title>Amber Kite — Splash</title>
<link href="https://fonts.googleapis.com/css2?family=Roboto:wght@400;500&family=Rubik:wght@900&display=swap" rel="stylesheet">
<style>
  :root {
    --brand-red: #ec2027;
    --header-red: #d4151c;
    --header-red-dark: #c10f17;
    --white: #ffffff;
    --sun-light: #fff3b0;
    --sun-mid: #ffd23a;
    --sun-deep: #fbb829;
    --tab-orange: #f7870b;
    --swoosh-orange: #f7a22c;
    --swoosh-line: #f08a1c;
    --grid-line: rgba(230, 150, 20, 0.18);
    --back-black: #1a1a1a;
    --icon-fill: #d8232a;
  }
  * { box-sizing: border-box; margin: 0; padding: 0; }
  html, body { width: 1200px; height: 809px; overflow: hidden; }
  body { font-family: "Roboto", Arial, sans-serif; }

  .splash {
    position: relative;
    width: 1200px;
    height: 809px;
    overflow: hidden;
    background:
      repeating-linear-gradient(90deg, transparent 0 140px, var(--grid-line) 140px 142px),
      repeating-linear-gradient(0deg, transparent 0 140px, var(--grid-line) 140px 142px),
      radial-gradient(ellipse 520px 420px at 600px 330px, var(--sun-light) 0%, var(--sun-mid) 50%, var(--sun-deep) 100%);
  }

  .swoosh { position: absolute; inset: 0; width: 1200px; height: 809px; }

  .top-bar {
    position: absolute; left: 0; top: 0;
    width: 1200px; height: 125px;
    background: linear-gradient(180deg, var(--header-red) 0%, var(--header-red-dark) 100%);
    border-bottom: 3px solid var(--brand-red);
  }

  .back-button {
    position: absolute; left: 39px; top: 35px;
    width: 130px; height: 65px;
    background: linear-gradient(180deg, #333 0%, var(--back-black) 55%, #000 100%);
    clip-path: polygon(26px 0, 100% 0, 100% 100%, 26px 100%, 0 50%);
    border-radius: 0 5px 5px 0;
    color: var(--white);
    font-size: 26px;
    font-weight: 400;
    display: flex; align-items: center; justify-content: center;
    padding-left: 22px;
  }

  .product-title {
    position: absolute; left: 0; top: 20px; width: 1200px;
    text-align: center;
    font-family: "Rubik", Arial, sans-serif;
    font-weight: 900;
    font-size: 68px;
    line-height: 80px;
    color: var(--white);
  }

  .product-icon {
    position: absolute; left: 432px; top: 154px;
    width: 336px; height: 336px; border-radius: 50%;
    background: var(--icon-fill);
  }

  .group-list { position: absolute; left: 0; top: 187px; list-style: none; }
  .group-button {
    width: 193px; height: 78px; margin-bottom: 8px;
    background: var(--tab-orange);
    border-radius: 0 8px 8px 0;
    color: var(--white);
    font-size: 22px;
    display: flex; align-items: center;
    padding-left: 20px;
  }

  .instructions { position: absolute; left: 231px; top: 509px; width: 941px; }
  .instruction {
    display: flex; align-items: center;
    height: 87px; margin-bottom: 13px;
    background: var(--brand-red);
    border-radius: 7px;
    padding: 0 18px 0 14px;
    color: var(--white);
    font-size: 25.5px; line-height: 32px;
  }
  .instruction svg { flex: 0 0 34px; margin-right: 12px; align-self: flex-start; margin-top: 22px; }

  .company-name {
    position: absolute; right: 32px; top: 734px;
    font-size: 42px; font-weight: 400;
    color: var(--brand-red);
    line-height: 52px;
  }
</style>
</head>
<body>
<main class="splash">
  <svg class="swoosh" viewBox="0 0 1200 809" aria-hidden="true">
    <path d="M955 125 C1080 300 1140 520 1150 809 L1200 809 L1200 125 Z" fill="var(--swoosh-orange)" opacity="0.75"/>
    <path d="M955 125 C1080 300 1140 520 1150 809" fill="none" stroke="var(--swoosh-line)" stroke-width="3"/>
  </svg>

  <header class="top-bar">
    <div class="back-button">Back</div>
    <h1 class="product-title">Amber Kite</h1>
  </header>

  <div class="product-icon" role="img" aria-label="Product icon placeholder: red sphere with the white letters AK"></div>

  <ul class="group-list">
    <li class="group-button">Gender, viday</li>
    <li class="group-button">Gender, today</li>
    <li class="group-button">geo, viday</li>
    <li class="group-button">Gender, viday</li>
    <li class="group-button">Gender, mpst</li>
    <li class="group-button">geo, mpst</li>
  </ul>

  <section class="instructions">
    <p class="instruction">
      <svg width="34" height="28" viewBox="0 0 34 28" aria-hidden="true"><path d="M3 15 L12 24 L31 4" fill="none" stroke="var(--white)" stroke-width="6" stroke-linecap="round" stroke-linejoin="round"/></svg>
      <span>Press the button for the type of prediction you would like to see in order to view the most up-to-date predictions for each group within that type.</span>
    </p>
    <p class="instruction">
      <svg width="34" height="28" viewBox="0 0 34 28" aria-hidden="true"><path d="M3 15 L12 24 L31 4" fill="none" stroke="var(--white)" stroke-width="6" stroke-linecap="round" stroke-linejoin="round"/></svg>
      <span>You can also view past predictions for a given group by simply pressing the button for that group.</span>
    </p>
  </section>

  <div class="company-name">Plorvex</div>
</main>
</body>
</html>
```